Corvane Transit Assoc needs Info graphic 1 pager (front & back)

We are looking for design work for an infographic type 1 pager (front and back). We will provide the information for the project. I need your help in the layout. Please see attachments for a general idea and direction. I value your design ideas, though, so please feel free to add your personal touch.

Front page is the new infographic that you are creating based off of my hand drafted sketch.

Back page is simply using the Flowchart from the Tellis Review Bureau.

Target Market(s)

State Legislators

Industry/Entity Type

Work

Requirements
Must have
• Nice looking info graphic one-pager. Please try to use the photos I sent in the graphic or similar rail clip art. Make the numbers stand out where possible. Give them emphasis.
• Make it clean. I want to share this info in short/quick meetings with legislators. I want it easy to decipher.
Nice to have
• Bold, strong colors.

```html
<!DOCTYPE html>
<html lang="en">
<head>
<meta charset="utf-8">
<title>Public Act 51 of 1951 – Freight Railroad Funding</title>
<link href="https://fonts.googleapis.com/css2?family=Anton&family=Oswald:wght@300;400;500;600&family=Arimo:ital,wght@0,400;0,700;1,400&display=swap" rel="stylesheet">
<style>
  :root{
    --backdrop:#e7e2da;
    --white:#ffffff;
    --ink:#141414;
    --orange:#f26722;
    --brick:#9b1c1f;
    --brick-dark:#861619;
    --tan:#e3c08b;
    --tan-light:#f0dcb5;
    --cream-circle:rgba(253,236,180,.9);
    --yellow:#fbe43a;
    --yellow-light:#fff27a;
    --navy:#1f2a5a;
    --paper:#fdf6e5;
    --highlight:#fff200;
    --chart-line:#111;
  }
  *{box-sizing:border-box;margin:0;padding:0}
  html,body{width:1200px;height:1200px;overflow:hidden;background:var(--backdrop)}
  body{position:relative;font-family:"Oswald",sans-serif}

  .sheet{position:absolute;top:208px;width:555px;height:784px;box-shadow:0 4px 14px rgba(0,0,0,.18);overflow:hidden}
  .sheet--front{left:26px;background:var(--white)}
  .sheet--back{left:614px;background:var(--paper)}
  .front{position:absolute;left:0;top:0;width:694px;height:980px;transform:scale(.8);transform-origin:0 0}
  .abs{position:absolute}

  /* header */
  .title{left:0;top:14px;width:694px;text-align:center;font-family:"Anton",sans-serif;font-size:74px;line-height:1;letter-spacing:1px;color:var(--ink)}
  .subtitle{left:0;top:92px;width:694px;text-align:center;font-weight:300;font-size:44px;line-height:1;color:var(--ink)}
  .subtitle .star{color:var(--brick);font-size:46px;margin:0 14px}
  .rule-red{left:0;top:155px;width:694px;height:8px;background:var(--brick)}
  .rule-tan{left:0;top:163px;width:694px;height:12px;background:var(--tan)}

  /* photo panel */
  .photo{left:0;top:175px;width:420px;height:435px;background:linear-gradient(160deg,#b8c6cf 0%,#6f8ca3 35%,#8c8170 70%,#c9a77a 100%)}
  .ctf-heading{left:22px;top:182px;font-family:"Anton",sans-serif;font-size:33px;line-height:.98;color:var(--ink)}
  .ctf-sub{left:22px;top:250px;font-size:24px;line-height:1;color:var(--ink);font-weight:500}
  .ctf-sub em{font-style:normal;color:var(--orange)}
  .ctf-sub small{font-size:19px}
  .ctf-circle{left:66px;top:282px;width:300px;height:300px;border-radius:50%;background:var(--cream-circle)}
  .ctf-label{left:66px;top:300px;width:300px;text-align:center;font-family:"Anton",sans-serif;font-size:50px;line-height:1;color:var(--ink)}
  .ctf-amount{left:66px;top:356px;width:300px;text-align:center;font-size:28px;color:var(--ink)}
  .rail-label{left:90px;top:462px;width:116px;text-align:right;font-size:25px;line-height:1.1;color:var(--orange);font-weight:500}
  .rail-pct{left:228px;top:436px;font-size:86px;line-height:1;color:var(--orange);font-weight:500}
  .bullet{font-size:19px;line-height:1.05;color:#fdf3df;font-weight:400}
  .bullet::before{content:"";display:inline-block;width:11px;height:11px;border-radius:50%;background:var(--orange);margin-right:5px;vertical-align:1px}
  .bullet--left{left:22px;top:540px}
  .bullet--right{left:270px;top:540px;width:145px;text-align:right}

  /* stat boxes */
  .stat{left:425px;width:269px;height:100px;color:var(--white);display:flex;align-items:center;padding:0 14px;gap:14px}
  .stat--orange{background:var(--orange)}
  .stat--budget{top:178px}
  .stat--share{top:288px}
  .stat--autos{top:398px;background:var(--white);border:4px solid var(--brick);color:var(--brick)}
  .big-num{font-size:72px;line-height:.9;font-weight:500}
  .big-num .unit{display:block;font-size:27px;line-height:1;margin-top:2px}
  .stat-text{font-size:30px;line-height:1}
  .stat-text--small{font-size:19px;line-height:.98}
  .stat-text--bold{font-family:"Anton",sans-serif;font-size:19px;line-height:.98}
  .mini{top:508px;height:100px;background:var(--brick-dark);color:var(--white);text-align:center;padding-top:4px}
  .mini--rail{left:425px;width:133px}
  .mini--miles{left:568px;width:126px}
  .mini .num{font-size:44px;line-height:1;font-weight:500}
  .mini .lbl{font-size:18px;line-height:.95}

  /* safety */
  .safety-band{left:0;top:625px;width:694px;height:63px;background:var(--ink)}
  .safety-title{left:150px;top:622px;width:430px;text-align:center;font-family:"Anton",sans-serif;font-size:58px;line-height:1.1;color:var(--yellow)}
  .safety-title .stars{color:#fdf3df;font-size:36px;vertical-align:10px;margin:0 14px;letter-spacing:4px}
  .safety-panel{left:0;top:688px;width:694px;height:147px;background:linear-gradient(180deg,var(--tan) 0%,var(--tan-light) 60%,#dcb380 100%)}
  .crossbuck{left:16px;top:630px;width:100px;height:100px;background:#f4efe4;opacity:.95}
  .signal{left:12px;top:735px;width:110px;height:50px;background:#3a3a3a;border-radius:25px}
  .rr-sign{left:566px;top:628px;width:118px;height:118px;border-radius:50%;background:var(--yellow)}
  .divider-v{left:345px;top:688px;width:5px;height:147px;background:var(--navy)}
  .program-title{width:220px;text-align:center;font-family:"Anton",sans-serif;font-size:24px;line-height:1;color:var(--brick)}
  .program-title--crossing{left:120px;top:704px}
  .program-title--surface{left:362px;top:704px;width:230px}
  .program-amt{font-family:"Anton",sans-serif;font-size:52px;line-height:1;color:var(--ink)}
  .program-amt small{font-family:"Oswald",sans-serif;font-size:32px;font-weight:500}
  .program-amt--crossing{left:120px;top:758px}
  .program-amt--surface{left:362px;top:758px}
  .program-desc{font-size:14px;line-height:1.02;color:var(--ink);font-weight:500}
  .program-desc--crossing{left:210px;top:762px;width:132px}
  .program-desc--surface{left:452px;top:762px;width:150px}

  /* footer */
  .rule-navy{left:0;top:835px;width:694px;height:6px;background:var(--navy)}
  .org{left:0;top:841px;width:170px;height:139px;background:var(--white);text-align:center;padding-top:28px;color:var(--navy)}
  .org-name{font-size:25px;line-height:1.05;font-weight:600;letter-spacing:1px}
  .org-phone{margin-top:18px;font-size:20px;font-weight:600;color:var(--ink)}
  .footer-divider{left:170px;top:841px;width:8px;height:139px;background:var(--navy)}
  .footer-yellow{left:188px;top:852px;width:506px;height:124px;background:linear-gradient(90deg,var(--yellow) 0%,var(--yellow-light) 50%,var(--yellow) 100%)}
  .footer-rail{left:200px;top:884px;width:140px;text-align:center;font-family:"Anton",sans-serif;font-size:27px;line-height:1;color:var(--brick)}
  .footer-eq{left:335px;top:880px;font-family:"Anton",sans-serif;font-size:48px;line-height:1;color:var(--brick)}
  .seal{left:366px;top:848px;width:130px;height:130px}
  .footer-total{left:490px;top:870px;width:200px;text-align:center;font-family:"Anton",sans-serif;font-size:27px;line-height:1;color:var(--brick)}

  /* back */
  .flowchart{position:absolute;left:0;top:0;width:555px;height:784px}
  .fc{font-family:"Arimo",sans-serif;fill:var(--ink)}
</style>
</head>
<body>

<section class="sheet sheet--front" aria-label="Front: freight railroad funding infographic">
  <div class="front">
    <h1 class="abs title">PUBLIC ACT 51 OF 1951</h1>
    <p class="abs subtitle"><span class="star">★</span>FREIGHT RAILROAD FUNDING<span class="star">★</span></p>
    <div class="abs rule-red"></div>
    <div class="abs rule-tan"></div>

    <div class="abs photo" role="img" aria-label="Photo of a freight locomotive on the tracks"></div>
    <h2 class="abs ctf-heading">COMPREHENSIVE<br>TRANSPORTATION FUND</h2>
    <p class="abs ctf-sub">“UP TO <em>10%</em> OF MTF” <small>Sec. 10(1)(h)</small></p>
    <div class="abs ctf-circle"></div>
    <p class="abs ctf-label">CTF</p>
    <p class="abs ctf-amount">$320.5m</p>
    <svg class="abs" style="left:0;top:0" width="420" height="610" aria-hidden="true">
      <polygon points="204,580 228,580 216,430" fill="var(--orange)"/>
    </svg>
    <p class="abs rail-label">FREIGHT<br>RAIL</p>
    <p class="abs rail-pct">2%</p>
    <p class="abs bullet bullet--left">FREIGHT<br>ECONOMIC<br>DEVELOPMENT</p>
    <p class="abs bullet bullet--right">FREIGHT<br>PROPERTY<br>MANAGEMENT</p>

    <div class="abs stat stat--orange stat--budget">
      <p class="big-num">$4.1<span class="unit">BILLION</span></p>
      <p class="stat-text">MDOT<br>BUDGET</p>
    </div>
    <div class="abs stat stat--orange stat--share">
      <p class="big-num">20%</p>
      <p class="stat-text stat-text--small">PORTION<br>OF FREIGHT<br>MOVED BY<br>RAIL IN MI</p>
    </div>
    <div class="abs stat stat--autos">
      <p class="big-num">75%</p>
      <p class="stat-text stat-text--bold">OF ALL NEW<br>AUTOMOBILES<br>LEAVE<br>MI ON RAIL</p>
    </div>
    <div class="abs mini mini--rail"><p class="num">28</p><p class="lbl">FREIGHT<br>RAILROADS<br>IN MI</p></div>
    <div class="abs mini mini--miles"><p class="num">3,600</p><p class="lbl">MILES OF<br>TRACKS</p></div>

    <div class="abs safety-band"></div>
    <div class="abs safety-panel"></div>
    <div class="abs crossbuck" role="img" aria-label="Railroad crossbuck sign illustration"></div>
    <h2 class="abs safety-title"><span class="stars">★★★</span>SAFETY<span class="stars">★★★</span></h2>
    <div class="abs rr-sign" role="img" aria-label="Round railroad advance warning sign illustration"></div>
    <div class="abs signal" role="img" aria-label="Crossing signal lights illustration"></div>
    <div class="abs divider-v"></div>

    <h3 class="abs program-title program-title--crossing">CROSSING<br>SAFETY PROGRAM</h3>
    <p class="abs program-amt program-amt--crossing">$3<small>m</small></p>
    <p class="abs program-desc program-desc--crossing">PROVIDES FUNDS FOR THE ELIMINATION OF HAZARDS AT RAILWAY-HIGHWAY CROSSINGS</p>

    <h3 class="abs program-title program-title--surface">LOCAL SURFACE<br>GRADE CROSSING</h3>
    <p class="abs program-amt program-amt--surface">$3<small>m</small></p>
    <p class="abs program-desc program-desc--surface">HELPS LOCALS / RAILROADS PARTNER TO BETTER MAINTAIN LOCAL CROSSING SURFACES FOR THE MOTORING PUBLIC</p>

    <div class="abs rule-navy"></div>
    <div class="abs org">
      <p class="org-name">CORVANE<br>TRANSIT ASSOC</p>
      <p class="org-phone">PH 555.014.2290</p>
    </div>
    <div class="abs footer-divider"></div>
    <div class="abs footer-yellow"></div>
    <p class="abs footer-rail">FREIGHT<br>RAILROADS</p>
    <p class="abs footer-eq">=</p>
    <svg class="abs seal" viewBox="0 0 130 130" aria-hidden="true">
      <polygon fill="#fff" stroke="#111" stroke-width="3" points="65,4 73,15 85,8 89,21 103,19 103,33 116,36 111,49 123,56 114,66 123,76 111,82 116,95 103,98 103,112 89,110 85,123 73,116 65,126 57,116 45,123 41,110 27,112 27,98 14,95 19,82 7,76 16,66 7,56 19,49 14,36 27,33 27,19 41,21 45,8 57,15"/>
      <text x="64" y="92" text-anchor="middle" font-family="Oswald, sans-serif" font-weight="500" font-size="74" fill="var(--brick)">1%</text>
    </svg>
    <p class="abs footer-total">OF TOTAL<br>TRANSPORTATION<br>BUDGET</p>
  </div>
</section>

<section class="sheet sheet--back" aria-label="Back: transportation fund distribution flowchart">
  <svg class="flowchart" viewBox="0 0 694 980">
    <defs>
      <marker id="arrow" viewBox="0 0 10 10" refX="9" refY="5" markerWidth="6" markerHeight="6" orient="auto">
        <path d="M0,0 L10,5 L0,10 z" fill="#111"/>
      </marker>
    </defs>
    <g class="fc" text-anchor="middle">
      <text x="385" y="56" font-size="11" font-weight="700">FY 2016-17 MICHIGAN TRANSPORTATION FUND REVENUES AND</text>
      <text x="385" y="69" font-size="11" font-weight="700">DISTRIBUTIONS PER Sec. 10, 1951 PA 51</text>
      <text x="385" y="81" font-size="7.5" font-style="italic">January 2016 ORTA Estimate</text>
    </g>

    <!-- connectors -->
    <g stroke="#111" stroke-width="1.4" fill="none">
      <line x1="370" y1="168" x2="370" y2="468"/>
      <line x1="370" y1="468" x2="395" y2="468" marker-end="url(#arrow)"/>
      <line x1="370" y1="204" x2="325" y2="204" marker-end="url(#arrow)"/>
      <line x1="370" y1="258" x2="325" y2="258" marker-end="url(#arrow)"/>
      <line x1="370" y1="312" x2="325" y2="312" marker-end="url(#arrow)"/>
      <line x1="370" y1="448" x2="325" y2="448" marker-end="url(#arrow)"/>
      <line x1="370" y1="235" x2="414" y2="235" marker-end="url(#arrow)"/>
      <line x1="370" y1="334" x2="414" y2="334" marker-end="url(#arrow)"/>
      <line x1="128" y1="378" x2="170" y2="346" marker-end="url(#arrow)"/>
      <line x1="585" y1="497" x2="585" y2="727"/>
      <line x1="585" y1="562" x2="533" y2="562" marker-end="url(#arrow)"/>
      <line x1="585" y1="642" x2="473" y2="642" marker-end="url(#arrow)"/>
      <line x1="585" y1="727" x2="406" y2="727" marker-end="url(#arrow)"/>
      <line x1="75" y1="684" x2="129" y2="730" marker-end="url(#arrow)"/>
    </g>

    <!-- MTF -->
    <rect x="140" y="88" width="490" height="80" rx="10" fill="#e6e6e6" stroke="#111" stroke-width="4"/>
    <rect x="146" y="94" width="478" height="68" rx="7" fill="none" stroke="#111" stroke-width="1"/>
    <g class="fc" text-anchor="middle" font-size="8">
      <text x="385" y="110" font-weight="700">MICHIGAN TRANSPORTATION FUND (MTF)</text>
      <line x1="146" y1="117" x2="624" y2="117" stroke="#111"/>
      <text x="385" y="130">MTF Revenue = <tspan font-weight="700">$2,514,863,000</tspan></text>
      <text x="385" y="142">Less $21,466,200 to DNR <tspan font-style="italic">Recreation</tspan> Improvement Fund</text>
      <text x="385" y="154">Net MTF Revenue = <tspan font-weight="700">$2,493,396,800</tspan></text>
    </g>

    <!-- left column -->
    <g fill="#fff" stroke="#111" stroke-width="1.2">
      <rect x="132" y="180" width="191" height="46"/>
      <rect x="132" y="235" width="191" height="46"/>
      <rect x="132" y="288" width="191" height="47"/>
      <rect x="132" y="427" width="191" height="43"/>
      <rect x="32" y="332" width="93" height="98" rx="12"/>
      <rect x="20" y="577" width="100" height="107" rx="12"/>
    </g>
    <g class="fc" text-anchor="middle" font-size="7.5">
      <text x="227" y="194" font-weight="700" font-style="italic">MDOT Local Agency Programs, Planning,</text>
      <text x="227" y="204" font-weight="700" font-style="italic">Administration, Rail Safety</text>
      <text x="227" y="216" font-weight="700">$28,189,000</text>
      <text x="227" y="249" font-weight="700" font-style="italic">To Other State Departments</text>
      <text x="227" y="260" font-weight="700">$24,335,000</text>
      <text x="227" y="272">(collection and other support costs)</text>
      <text x="227" y="302" font-weight="700" font-style="italic">Comprehensive Transportation Fund</text>
      <text x="227" y="314" font-weight="700">$220,661,400</text>
      <text x="227" y="326" font-style="italic">(10% of net MTF after above deductions)</text>
      <text x="227" y="439" font-weight="700" font-style="italic">Statutory Grants</text>
      <text x="78" y="356" font-size="7" font-weight="700" font-style="italic">Sales Tax</text>
      <text x="78" y="367" font-size="7" font-weight="700" font-style="italic">$94,800,000</text>
      <text x="78" y="378" font-size="7" font-style="italic">CTF also receives</text>
      <text x="78" y="389" font-size="7" font-style="italic">earmark from</text>
      <text x="78" y="400" font-size="7" font-style="italic">motor vehicle</text>
      <text x="78" y="411" font-size="7" font-style="italic">related sales tax</text>
      <text x="70" y="596" font-size="7" font-weight="700" font-style="italic">TEDF Transfer</text>
      <text x="70" y="607" font-size="7" font-weight="700" font-style="italic">$10,400,000</text>
      <text x="70" y="618" font-size="7" font-style="italic">House Bill 4440</text>
      <text x="70" y="629" font-size="7" font-style="italic">(2016 PA 273)</text>
      <text x="70" y="640" font-size="7" font-style="italic">redirected $10.4</text>
      <text x="70" y="651" font-size="7" font-style="italic">million from TEDF</text>
      <text x="70" y="662" font-size="7" font-style="italic">Category A</text>
      <text x="70" y="673" font-size="7" font-style="italic">program to the STF</text>
    </g>
    <g class="fc" font-size="7">
      <text x="140" y="451">Local Bridge Fund</text><text x="315" y="451" text-anchor="end">$ 5,000,000</text>
      <text x="140" y="462">Local Program Fund</text><text x="315" y="462" text-anchor="end">$33,000,000</text>
    </g>

    <!-- right column -->
    <g fill="#fff" stroke="#111" stroke-width="1.2">
      <rect x="416" y="173" width="220" height="124"/>
      <rect x="416" y="303" width="220" height="62"/>
      <rect x="397" y="438" width="239" height="59"/>
    </g>
    <g fill="var(--highlight)">
      <rect x="428" y="227" width="200" height="9"/>
      <rect x="428" y="238" width="200" height="9"/>
      <rect x="428" y="249" width="200" height="9"/>
      <rect x="559" y="472" width="70" height="9"/>
      <rect x="559" y="483" width="70" height="9"/>
    </g>
    <g class="fc" font-size="7">
      <text x="526" y="186" text-anchor="middle" font-size="7.5" font-weight="700" font-style="italic">Statutory Grants</text>
      <text x="430" y="199">Rail Grade Crossing</text><text x="628" y="199" text-anchor="end">$ 3,000,000</text>
      <text x="430" y="210">Rail Grade Surface Program</text><text x="628" y="210" text-anchor="end">$ 3,000,000</text>
      <text x="430" y="221">Local Bridge Fund Debt Service</text><text x="628" y="221" text-anchor="end">$ 2,406,800</text>
      <text x="430" y="234">3 cent of Gas Tax</text><text x="628" y="234" text-anchor="end">$117,889,500</text>
      <text x="430" y="245"># Local Wetland Mitigation Fund</text><text x="628" y="245" text-anchor="end">$ 4,000,000</text>
      <text x="430" y="256"># Movable Bridge Fund</text><text x="628" y="256" text-anchor="end">$ 10,000,000</text>
      <text x="430" y="267">½ cent for State Trunkline Bridges</text><text x="628" y="267" text-anchor="end">$ 21,981,600</text>
      <text x="430" y="278">½ cent for Local Bridges</text><text x="628" y="278" text-anchor="end">$ 21,981,600</text>
      <text x="430" y="289">STF Debt Reduction</text><text x="628" y="289" text-anchor="end">$ 50,000,000</text>
    </g>
    <g class="fc" text-anchor="middle" font-size="7.5">
      <text x="526" y="320" font-weight="700" font-style="italic">Transportation Economic Development Fund</text>
      <text x="526" y="332" font-weight="700">$40,275,000</text>
      <text x="526" y="344" font-style="italic">($36,775,000 + $3,500,000 earmarked for</text>
      <text x="526" y="355" font-style="italic">Targeted industries)</text>
      <text x="516" y="455" font-weight="700">MTF BALANCE = $1,907,676,900</text>
      <text x="516" y="467" font-size="7" font-style="italic">plus</text>
    </g>
    <g class="fc" font-size="7">
      <text x="412" y="479">3¢ of Gas Tax (see above)</text><text x="627" y="479" text-anchor="end">$ 117,889,500</text>
      <text x="412" y="490" font-weight="700" font-style="italic">Total to Distribute by Formula</text><text x="627" y="490" text-anchor="end" font-weight="700">$2,025,566,400</text>
    </g>

    <!-- formula recipients -->
    <g fill="#fff" stroke="#111" stroke-width="1.2">
      <rect x="272" y="525" width="258" height="72" rx="8"/>
      <rect x="212" y="605" width="258" height="72" rx="8"/>
      <rect x="133" y="686" width="270" height="84" rx="8"/>
    </g>
    <g fill="var(--highlight)">
      <rect x="356" y="546" width="90" height="9"/>
      <rect x="425" y="568" width="52" height="9"/>
      <rect x="296" y="626" width="90" height="9"/>
      <rect x="358" y="648" width="52" height="9"/>
      <rect x="222" y="707" width="90" height="9"/>
      <rect x="286" y="729" width="52" height="9"/>
    </g>
    <g class="fc" text-anchor="middle" font-size="7">
      <text x="401" y="541" font-size="7.5" font-weight="700">COUNTY ROAD COMMISSIONS</text>
      <text x="401" y="553" font-weight="700">Total = $813,182,500</text>
      <text x="401" y="564">39.1 % of MTF Balance    $745,901,700</text>
      <text x="401" y="575">39.1% of 3¢ Gas Tax          $ 46,094,800</text>
      <text x="401" y="587">Plus $21,186,000 from the Local Program Fund</text>

      <text x="341" y="621" font-size="7.5" font-weight="700">CITIES AND VILLAGES</text>
      <text x="341" y="633" font-weight="700">Total = $453,387,500</text>
      <text x="341" y="644">21.8% of MTF Balance  $415,873,600</text>
      <text x="341" y="655">21.8% of 3¢ Gas Tax        $ 25,699,900</text>
      <text x="341" y="667">Plus $11,814,000 from the Local Program Fund</text>

      <text x="268" y="702" font-size="7.5" font-weight="700">STATE TRUNKLINE FUND</text>
      <text x="268" y="714" font-weight="700">Total = $863,978,100</text>
      <text x="268" y="725">39.1 % of MTF Balance    $745,901,700</text>
      <text x="268" y="736">39.1% of 3¢ Gas Tax          $ 46,094,800</text>
      <text x="268" y="747">Plus $21,981,600 from ½ cent of gas tax for STF bridges</text>
      <text x="268" y="758">and $50,000,000 for STF Debt Reduction</text>
    </g>

    <!-- note -->
    <g class="fc" font-size="7.6">
      <text x="118" y="798"># Note:  This flowchart represents the distribution of MTF revenue as guided by Section 10 of Public Act 51 of 1951, as</text>
      <text x="118" y="811">amended by Public Act 246 of 2016.  Public Act 246 established two new earmarks of MTF revenue: $2.0 million for a</text>
      <text x="118" y="824">new Local agency wetland mitigation bank fund, and $5.0 million for a new Movable bridge fund, effective September</text>
      <text x="118" y="837">22, 2016.  For FY 2016-17 the earmarks are twice the fixed statutory amounts because both FY 2015-16 and FY 2016-</text>
      <text x="118" y="850">17 earmarks were appropriated in single year, FY 2016-17, in supplemental appropriation act, Public Act 340 of 2016.</text>
      <text x="74" y="900" font-size="8.5">Daniel R. Osterly</text>
      <text x="74" y="914" font-size="8.5">February 1, 2017</text>
    </g>
    <g class="fc">
      <rect x="555" y="872" width="130" height="48" fill="#fff"/>
      <text x="620" y="893" text-anchor="middle" font-family="Oswald, sans-serif" font-weight="600" font-size="13">TELLIS REVIEW</text>
      <text x="620" y="911" text-anchor="middle" font-family="Oswald, sans-serif" font-weight="600" font-size="13">BUREAU</text>
    </g>
  </svg>
</section>

</body>
</html>
```